Brand New Upscale OOBGYN Office

Im in Need of an advertising one sided postcard as soon as possible. It's for a brand new OBGYN office in the Northern Virginia area. We are trying to create a new patient customer base. I have attached photos of the inside of the office and logos. The office contact information needs to be on the postcard. You can find that on the attached pdf file named business card. That same file is the font that needs to be used. The font is called TT Drugs. Please contact me with any questions. I would appreciated it so much if you could send me these proofs as soon as possible. Thank you!!!
Women
Advertising
- TT Drugs

```html
<!DOCTYPE html>
<html lang="en">
<head>
<meta charset="utf-8">
<title>Laurel Vale OBGYN – Postcard</title>
<link rel="stylesheet" href="https://fonts.googleapis.com/css2?family=Poppins:wght@300;400&family=Oswald:wght@300;400&display=swap">
<style>
  :root{
    --slate:#6d6e71;
    --sage:#e2ebc2;
    --ink:#231f20;
    --white:#ffffff;
    --icon:#e2ebc2;
  }
  *{margin:0;padding:0;box-sizing:border-box}
  html,body{width:1200px;height:848px;overflow:hidden;background:var(--white)}
  .postcard{position:relative;width:1200px;height:848px;overflow:hidden;font-family:"Poppins",sans-serif;color:var(--ink)}
  .shapes{position:absolute;inset:0}
  .brand{position:absolute;left:730px;top:52px;display:flex;align-items:center;gap:18px}
  .brand-mark{width:84px;height:84px;border-radius:50%;background:var(--slate)}
  .brand-name{font-weight:300;font-size:27px;letter-spacing:1px;color:var(--slate);line-height:1.15;text-transform:uppercase}
  .brand-name small{display:block;font-size:19px;text-transform:none;letter-spacing:3px;border-top:1px solid var(--slate);padding-top:2px;margin-top:4px}
  .headline{position:absolute;right:44px;top:168px;text-transform:uppercase;text-align:center;white-space:nowrap;font-weight:300}
  .headline-region{display:block;font-family:"Poppins",sans-serif;font-weight:300;font-size:30px;letter-spacing:2px;line-height:1.15}
  .headline-main{display:block;font-family:"Oswald",sans-serif;font-weight:300;font-size:32px;letter-spacing:.3px;line-height:1.3}
  .services-title{position:absolute;right:68px;top:488px;font-weight:300;font-size:36px;letter-spacing:1px}
  .service{position:absolute;font-weight:300;font-size:20px;text-transform:uppercase;text-align:right;line-height:1.1;display:flex;align-items:center;gap:10px;white-space:nowrap}
  .service::after{content:"";width:9px;height:9px;border-radius:50%;background:var(--slate);flex:none}
  .service.surgical{right:445px;top:552px}
  .service.infertility{right:445px;top:592px}
  .service.obstetric{right:68px;top:568px}
  .service.gynecologic{right:68px;top:636px}
  .contact{position:absolute;color:var(--white);font-weight:300;font-size:17px;text-align:right;line-height:1.35;white-space:nowrap}
  .contact-row{display:flex;align-items:center;justify-content:flex-end;gap:12px}
  .contact-row svg{flex:none}
  .contact.online{right:540px;top:728px}
  .contact.office{right:64px;top:752px}
  .contact-row+.contact-row{margin-top:4px}
</style>
</head>
<body>
<main class="postcard">
  <svg class="shapes" width="1200" height="848" viewBox="0 0 1200 848">
    <defs>
      <linearGradient id="familyTone" x1="0" y1="0" x2="1" y2="1">
        <stop offset="0" stop-color="#4a3f3a"/>
        <stop offset=".45" stop-color="#c99a8e"/>
        <stop offset="1" stop-color="#1c1a1a"/>
      </linearGradient>
      <linearGradient id="officeTone" x1="0" y1="0" x2="1" y2="0">
        <stop offset="0" stop-color="#d9d6d2"/>
        <stop offset=".5" stop-color="#a9b5bb"/>
        <stop offset="1" stop-color="#8a4a33"/>
      </linearGradient>
    </defs>
    <rect class="footer-band" x="0" y="690" width="1200" height="158" fill="var(--slate)"/>
    <rect class="services-field" x="0" y="462" width="1200" height="228" fill="var(--sage)"/>
    <rect class="office-photo" x="560" y="272" width="640" height="190" fill="url(#officeTone)" role="img" aria-label="Photo of the clinic reception area with front desk and wall clock"/>
    <rect class="header-panel" x="560" y="0" width="640" height="258" fill="var(--white)"/>
    <rect class="header-rule" x="560" y="258" width="640" height="14" fill="var(--slate)"/>
    <path class="sweep-slate" d="M0,0 H705 C695,380 480,700 80,848 H0 Z" fill="var(--slate)"/>
    <path class="sweep-line" d="M705,0 C695,380 480,700 80,848" fill="none" stroke="var(--white)" stroke-width="6"/>
    <path class="sweep-sage" d="M0,0 H655 C645,340 440,620 0,725 Z" fill="var(--sage)"/>
    <path class="family-photo" d="M0,0 H655 C635,290 410,555 0,645 Z" fill="url(#familyTone)" role="img" aria-label="Photo of two young girls hugging their pregnant mother's belly"/>
  </svg>

  <div class="brand">
    <span class="brand-mark"></span>
    <div class="brand-name">Laurel Vale OBGYN<small>physicians &amp; midwives</small></div>
  </div>

  <h1 class="headline">
    <span class="headline-region">Northern Virginia's</span>
    <span class="headline-main">Premiere Womens Health Center</span>
  </h1>

  <h2 class="services-title">OUR SERVICES</h2>
  <p class="service surgical">Surgical Services</p>
  <p class="service infertility"><span>Infertility<br>Services</span></p>
  <p class="service obstetric"><span>Obstetric and<br>Prenatal Services</span></p>
  <p class="service gynecologic"><span>Gynecologic<br>Services</span></p>

  <div class="contact online">
    <div class="contact-row">www.laurelvaleobgyn.com
      <svg width="18" height="18" viewBox="0 0 18 18" fill="none" stroke="var(--icon)" stroke-width="1.5"><circle cx="9" cy="9" r="7.5"/><ellipse cx="9" cy="9" rx="3.2" ry="7.5"/><path d="M1.5 9h15M3 5h12M3 13h12"/></svg>
    </div>
    <div class="contact-row">info@laurelvaleobgyn.com
      <svg width="18" height="14" viewBox="0 0 18 14"><rect width="18" height="14" rx="1" fill="var(--icon)"/><path d="M1 1l8 6 8-6" fill="none" stroke="var(--slate)" stroke-width="1.5"/></svg>
    </div>
  </div>

  <div class="contact office">
    <div class="contact-row">555-014-2267
      <svg width="20" height="20" viewBox="0 0 20 20" fill="none" stroke="var(--icon)" stroke-width="1.5"><circle cx="10" cy="10" r="8.5"/><path d="M7 5.5l1.5 2.5-1 1.2c.6 1.4 1.7 2.5 3.1 3.1l1.2-1 2.5 1.5-.8 1.8c-3.6-.2-7.1-3.7-7.3-7.3z" fill="var(--icon)"/></svg>
    </div>
    <div class="contact-row"><span>4120 Orchard Lane, Suite 305<br>Maple Grove, VA 20190</span>
      <svg width="20" height="18" viewBox="0 0 20 18" fill="none" stroke="var(--icon)" stroke-width="1.6"><path d="M2 9l8-7 8 7M4.5 7v9h11V7M8.5 16v-5h3v5"/></svg>
    </div>
  </div>
</main>
</body>
</html>
```